Postcard Design - Simple

Freight Factoring Company - We purchase freight invoices from trucking companies. We then pay them the same day so they don't have to wait 4-6 weeks to get their money.

Industry/Entity Type

It Company

```html
<!DOCTYPE html>
<html lang="en">
<head>
<meta charset="utf-8">
<title>Haulwise Capital – Postcard</title>
<link href="https://fonts.googleapis.com/css2?family=Oswald:wght@500&family=Lato:ital,wght@0,400;0,700;1,700&display=swap" rel="stylesheet">
<style>
  :root{
    --navy:#1f3f7e;
    --navy-dark:#17326a;
    --red:#c8192a;
    --charcoal:#333336;
    --ink:#2b2b2b;
    --paper:#ffffff;
    --stage:#ececec;
    --rule:#b9b9b9;
  }
  *{box-sizing:border-box;margin:0;padding:0}
  html,body{width:907px;height:1200px;overflow:hidden;background:var(--stage)}
  body{position:relative;font-family:'Lato',sans-serif;color:var(--ink)}

  .card{position:absolute;left:142px;width:653px;background:var(--paper);overflow:hidden}
  .card--front{top:62px;height:508px}
  .card--back{top:628px;height:507px}

  .slant{position:absolute;inset:0;width:100%;height:100%}

  /* front */
  .brand{position:absolute;left:30px;top:26px;display:flex;align-items:center;gap:8px;
    font-weight:700;font-size:19px;letter-spacing:.5px;color:#fff}
  .brand__dot{width:10px;height:10px;border-radius:50%;background:#fff}

  .headline{position:absolute;left:18px;top:84px;font-family:'Oswald',sans-serif;font-weight:500;
    font-size:44px;line-height:1;white-space:nowrap;transform:scaleX(.78);transform-origin:left top}
  .headline .hot{color:var(--red)}
  .headline .cool{color:var(--navy)}

  .offer{position:absolute;left:0;top:150px;width:340px;height:60px;background:var(--charcoal);
    padding:5px 0 0 20px;font-size:19px;line-height:26px;text-transform:uppercase;white-space:nowrap}
  .offer .line1{color:#fff}
  .offer .line2{color:#e3232f}

  .steps-title{position:absolute;left:17px;top:232px;font-size:16px;font-weight:700;color:var(--navy)}
  .steps{position:absolute;left:21px;top:260px;list-style:none;font-size:15px;line-height:19px;color:#333}
  .steps li{position:relative;padding-left:19px;margin-bottom:10px}
  .steps li::before,.details li::before{content:"";position:absolute;left:0;top:7px;width:7px;height:7px;border-radius:50%;background:var(--navy-dark)}
  .divider{position:absolute;left:28px;top:371px;width:250px;height:2px;
    background:linear-gradient(90deg,transparent,var(--rule),transparent)}

  .simple{position:absolute;left:17px;top:403px}
  .simple__big{font-size:16px;font-weight:700;font-style:italic;color:var(--red)}
  .simple__small{font-size:13px;font-weight:700;color:#222;margin-top:2px}

  .services{position:absolute;left:148px;top:381px;list-style:none}
  .services li{display:flex;align-items:center;gap:10px;height:34px;font-size:13px;color:#333;white-space:nowrap}
  .services svg{width:28px;height:28px;flex:none}

  .phone{position:absolute;display:flex;align-items:center;gap:7px;font-size:12px;color:#fff}
  .phone svg{width:11px;height:11px}
  .card--front .phone{left:18px;top:473px}

  .photo{position:absolute;left:0;top:0;width:100%;height:100%}
  .photo--freight{background:linear-gradient(160deg,#e8e8e8 0%,#9a9a9a 45%,#5a5a5a 100%);
    clip-path:polygon(395px 0,653px 0,653px 268px,340px 268px)}
  .photo--driver{background:linear-gradient(150deg,#3f78c4 0%,#2559a5 35%,#c9c9c9 65%,#8d8d8d 100%);
    clip-path:polygon(337px 275px,653px 275px,653px 508px,284px 508px)}

  /* back */
  .photo--handshake{background:linear-gradient(180deg,#f4f4f4 0%,#d9d9d9 55%,#c5b29e 80%,#e9e9e9 100%);
    clip-path:polygon(0 0,348px 0,325px 120px,0 120px)}
  .details-title{position:absolute;left:18px;top:134px;font-size:20px;font-weight:700;color:var(--red);letter-spacing:.2px}
  .details{position:absolute;left:20px;top:168px;list-style:none;font-size:13px;line-height:16px;color:#222}
  .details li{position:relative;padding-left:22px;margin-bottom:8.5px}
  .contact{position:absolute;left:17px;top:372px;font-size:13px;font-weight:700;color:#fff}
  .card--back .phone{left:18px;top:393px}
  .web{position:absolute;left:128px;top:393px;display:flex;align-items:center;gap:7px;font-size:12px;color:#fff}
  .web svg{width:11px;height:11px}

  .stamp{position:absolute;left:546px;top:62px;width:78px;height:100px;border:1px solid #9a9a9a}
  .address-line{position:absolute;left:375px;width:248px;height:1px;background:#a9a9a9}
</style>
</head>
<body>

<section class="card card--front">
  <div class="photo photo--freight" role="img" aria-label="Forklift loading a giant roll of dollar bills into a truck trailer"></div>
  <div class="photo photo--driver" role="img" aria-label="Smiling truck driver holding a business card in front of a blue truck"></div>

  <svg class="slant" viewBox="0 0 653 508" aria-hidden="true">
    <polygon points="0,0 380,0 366,70 0,70" fill="#1f3f7e"/>
    <polygon points="0,70 366,70 365,74 0,74" fill="#c8192a"/>
    <polygon points="0,468 130,468 145,496 292,496 290,508 0,508" fill="#1f3f7e"/>
    <polygon points="380,0 395,0 300,508 282,508" fill="#c8192a"/>
    <polygon points="395,0 402,0 307,508 300,508" fill="#ffffff"/>
    <polygon points="337,268 653,268 653,275 336,275" fill="#ffffff"/>
  </svg>

  <div class="brand"><span class="brand__dot"></span>HAULWISE CAPITAL</div>

  <h1 class="headline"><span class="hot">SPEED UP</span> <span class="cool">CASH FLOW !</span></h1>

  <div class="offer">
    <div class="line1">We buy freight invoices and</div>
    <div class="line2">Pay you the same day</div>
  </div>

  <h2 class="steps-title">Here’s how it works . .</h2>
  <ul class="steps">
    <li>You Deliver the Load</li>
    <li>You Send in Load Paperwork</li>
    <li>We Send Your Cash via<br>Direct Deposit on the Same Day</li>
  </ul>
  <div class="divider"></div>

  <div class="simple">
    <div class="simple__big">It’s that simple!</div>
    <div class="simple__small">We do the rest . . .</div>
  </div>

  <ul class="services">
    <li><svg viewBox="0 0 28 28"><circle cx="14" cy="14" r="13" fill="#c8192a"/><rect x="8" y="10" width="12" height="8" rx="1" fill="none" stroke="#fff" stroke-width="1.5"/><path d="M8 13h12" stroke="#fff" stroke-width="1.5"/></svg>Credit Checks</li>
    <li><svg viewBox="0 0 28 28"><circle cx="14" cy="14" r="13" fill="#c8192a"/><rect x="9" y="7" width="10" height="14" rx="1" fill="none" stroke="#fff" stroke-width="1.5"/><path d="M11 11h6M11 14h6M11 17h4" stroke="#fff" stroke-width="1.3"/></svg>Invoicing</li>
    <li><svg viewBox="0 0 28 28"><circle cx="14" cy="14" r="13" fill="#c8192a"/><circle cx="14" cy="16" r="5.5" fill="none" stroke="#fff" stroke-width="1.5"/><path d="M11 8h6l-2 3h-2z" fill="#fff"/><path d="M14 13v6" stroke="#fff" stroke-width="1.3"/></svg>Collections, etc.</li>
  </ul>

  <div class="phone"><svg viewBox="0 0 12 12"><path d="M2.5 1l2 2.3-1 1.3a6.5 6.5 0 0 0 3.9 3.9l1.3-1 2.3 2-1 1.5C5.5 11 1 6.5 1 2z" fill="#e3232f"/></svg>555-014-2290</div>
</section>

<section class="card card--back">
  <div class="photo photo--handshake" role="img" aria-label="Business handshake in front of a group of professionals"></div>

  <svg class="slant" viewBox="0 0 653 507" aria-hidden="true">
    <polygon points="0,120 325,120 324,124 0,124" fill="#1f3f7e"/>
    <polygon points="0,365 296,365 286,418 0,418" fill="#1f3f7e"/>
    <polygon points="0,362 297,362 296,365 0,365" fill="#c8192a"/>
    <polygon points="348,0 356,0 294,418 286,418" fill="#c8192a"/>
  </svg>

  <h2 class="details-title">HERE ARE THE DETAILS</h2>
  <ul class="details">
    <li>Short term contract</li>
    <li>No Setup Fees</li>
    <li>No Minimums</li>
    <li>Online 24 Hour Account Access</li>
    <li>Free Credit Checks</li>
    <li>Fuel Cards Available (Save 10 /gallon)</li>
    <li>Easy &amp; Quick Qualification</li>
    <li>We specialize in small fleets</li>
  </ul>

  <div class="contact">Contact Us Today At</div>
  <div class="phone"><svg viewBox="0 0 12 12"><path d="M2.5 1l2 2.3-1 1.3a6.5 6.5 0 0 0 3.9 3.9l1.3-1 2.3 2-1 1.5C5.5 11 1 6.5 1 2z" fill="#e3232f"/></svg>555-014-2290</div>
  <div class="web"><svg viewBox="0 0 12 12"><circle cx="6" cy="6" r="5" fill="none" stroke="#e3232f" stroke-width="1.4"/><path d="M1 6h10M6 1c2 2.5 2 7.5 0 10M6 1c-2 2.5-2 7.5 0 10" fill="none" stroke="#e3232f" stroke-width="1"/></svg>www.haulwisecapital.com</div>

  <div class="stamp"></div>
  <div class="address-line" style="top:262px"></div>
  <div class="address-line" style="top:309px"></div>
  <div class="address-line" style="top:356px"></div>
</section>

</body>
</html>
```